Brevik Seasoning
Brevik Seasoning - Food
Creative Brief
Simple
Tom Halvern
President and CEO
52190 Harlow Lane Sterling Heights, MI 48977
thalvern@brevikspice.com
Brevikspice.com
Xpert Xpert

```html
<!DOCTYPE html>
<html lang="en">
<head>
<meta charset="utf-8">
<title>Brevik Seasoning – Business Card</title>
<link rel="stylesheet" href="https://fonts.googleapis.com/css2?family=Playfair+Display:wght@700&family=Open+Sans:wght@400;600&display=swap">
<style>
  :root{
    --page:#e9e7e4;
    --card-dark:#0b0b0b;
    --card-light:#ffffff;
    --ink:#4a4a4a;
    --ink-soft:#7a7a7a;
    --accent-red:#d2232a;
    --spice-warm:#e0902a;
    --spice-deep:#c0432a;
  }
  *{box-sizing:border-box;margin:0;padding:0}
  html,body{width:1200px;height:904px;overflow:hidden}
  body{background:var(--page);font-family:"Open Sans",Arial,sans-serif;position:relative}

  .card{position:absolute;left:285px;width:630px;height:360px;box-shadow:0 6px 18px rgba(0,0,0,.18);overflow:hidden}
  .card--back{top:62px;background:var(--card-dark);display:flex;align-items:center;justify-content:center}
  .card--front{top:482px;background:var(--card-light)}

  .brand{display:flex;align-items:center;gap:10px}
  .brand__dot{width:16px;height:16px;border-radius:50%;background:var(--accent-red)}
  .brand__name{font-family:"Playfair Display",Georgia,serif;font-weight:700;font-size:34px;line-height:1;white-space:nowrap}
  .card--back .brand__name{color:#ffffff}
  .card--front .brand{position:absolute;left:38px;top:108px}
  .card--front .brand__name{color:#3a3a3a}

  .person{position:absolute;right:40px;top:30px;text-align:right}
  .person__name{color:var(--accent-red);font-weight:600;font-size:15px}
  .person__title{color:var(--ink-soft);font-size:12px;margin-top:2px}

  .address{position:absolute;left:40px;top:196px;color:var(--ink);font-size:12.5px;line-height:1.4}
  .contacts{position:absolute;left:40px;top:240px;list-style:none;color:var(--ink);font-size:12.5px;line-height:19px}
  .contacts li{display:flex;align-items:center;gap:8px}
  .contacts svg{width:12px;height:12px;fill:var(--ink-soft)}

  .swoop{position:absolute;right:0;top:0;width:260px;height:360px}
  .spice-art{position:absolute;right:34px;top:96px;width:160px;height:180px;border-radius:6px;
    background:linear-gradient(180deg,var(--spice-warm) 0%,var(--spice-deep) 100%)}
</style>
</head>
<body>

<section class="card card--back" aria-label="Card back">
  <div class="brand">
    <span class="brand__dot"></span>
    <span class="brand__name">Brevik Seasoning</span>
  </div>
</section>

<section class="card card--front" aria-label="Card front">
  <svg class="swoop" viewBox="0 0 260 360" aria-hidden="true">
    <path d="M260 120 C170 190 150 290 60 360 L260 360 Z" fill="var(--card-dark)"/>
  </svg>
  <div class="spice-art" role="img" aria-label="Illustration of colourful spice powders"></div>

  <div class="person">
    <p class="person__name">Tom Halvern</p>
    <p class="person__title">President and CEO</p>
  </div>

  <div class="brand">
    <span class="brand__dot"></span>
    <span class="brand__name">Brevik Seasoning</span>
  </div>

  <p class="address">52190 Harlow Lane<br>Sterling Heights, MI 48977</p>

  <ul class="contacts">
    <li><svg viewBox="0 0 12 12"><path d="M2.5 1l2 2.2-1 1.2c.7 1.5 1.7 2.5 3.1 3.1l1.2-1L10 8.5 9 11C4.5 10.6 1.4 7.5 1 3z"/></svg>586-555-0142</li>
    <li><svg viewBox="0 0 12 12"><path d="M3 0h6v12H3zM4 1.5v8h4v-8zM5.5 10.2h1v.8h-1z"/></svg>248-555-0187</li>
    <li><svg viewBox="0 0 12 12"><path d="M0 2h12v8H0zM1 3v.4l5 3.2 5-3.2V3zm0 1.6V9h10V4.6L6 7.8z"/></svg>thalvern@brevikspice.com</li>
    <li><svg viewBox="0 0 12 12"><path d="M6 0a6 6 0 100 12A6 6 0 006 0zm0 1c.7.8 1.2 2.2 1.3 4.5H4.7C4.8 3.2 5.3 1.8 6 1zM1 6.5h2.7c.1 1.6.4 3 .9 4A5 5 0 011 6.5zm0-1A5 5 0 014.6 1.5c-.5 1-.8 2.4-.9 4zm3.7 1h2.6C7.2 8.8 6.7 10.2 6 11c-.7-.8-1.2-2.2-1.3-4.5zm3.6 0H11a5 5 0 01-3.6 4c.5-1 .8-2.4.9-4zm0-1c-.1-1.6-.4-3-.9-4A5 5 0 0111 5.5z"/></svg>Brevikspice.com</li>
  </ul>
</section>

</body>
</html>
```